" Temos como propósito desenvolver pessoas e proporcionar saúde transformando vidas e sorrisos. Acreditamos que a educação muda pessoas e essas transformam o mundo. E que a manutenção da saúde bucal é fundamental para a saúde geral e o aumento da auto-estima do indivíduo. Nosso principal serviço são os cursos de ortodontia para dentistas já formados (pós-graduação e cursos livres de ortodontia). Temos alguns outros cursos também para dentistas em outras áreas. "

```html
<!DOCTYPE html>
<html lang="pt-BR">
<head>
<meta charset="UTF-8">
<title>Ortoplena – Papel Timbrado</title>
<link href="https://fonts.googleapis.com/css2?family=Montserrat:wght@400;500;600;700&display=swap" rel="stylesheet">
<style>
  :root {
    --backdrop: #e6e6e6;
    --paper: #ffffff;
    --navy: #2b4257;
    --ink: #4a4f55;
    --ink-soft: #8a8f95;
    --accent: #8c1f3f;
    --band-text: #ffffff;
    --signature-tone: #c9d0d8;
  }
  * { box-sizing: border-box; margin: 0; padding: 0; }
  html, body {
    width: 1200px; height: 1200px; overflow: hidden;
    background: var(--backdrop);
    font-family: "Montserrat", sans-serif;
  }
  .letterhead {
    position: absolute; left: 190px; top: 20px;
    width: 820px; height: 1160px;
    background: var(--paper);
    box-shadow: 0 6px 24px rgba(0,0,0,0.12);
  }
  .brand {
    position: absolute; left: 84px; top: 128px;
    font-size: 50px; font-weight: 600; letter-spacing: -0.5px;
    color: var(--navy);
  }
  .recipient {
    position: absolute; left: 100px; top: 300px;
    color: var(--ink);
  }
  .recipient__label { font-size: 13px; font-weight: 700; color: var(--navy); letter-spacing: 1px; }
  .recipient__name { font-size: 12px; font-weight: 700; color: var(--navy); margin-top: 4px; }
  .recipient__line { font-size: 9.5px; line-height: 15px; color: var(--ink-soft); }
  .letter-body {
    position: absolute; left: 100px; top: 430px; width: 620px;
    font-size: 10px; line-height: 15px; color: var(--ink);
  }
  .letter-body p + p { margin-top: 10px; }
  .signature {
    position: absolute; left: 100px; top: 770px;
    width: 160px; height: 44px;
    background: linear-gradient(90deg, var(--signature-tone), #e4e8ec);
    border-radius: 4px;
  }
  .signer { position: absolute; left: 100px; top: 832px; }
  .signer__name { font-size: 12px; font-weight: 700; color: var(--navy); }
  .signer__role { font-size: 9.5px; color: var(--ink-soft); margin-top: 2px; }
  .contact-band {
    position: absolute; left: 60px; right: 60px; top: 1030px; height: 50px;
    background: var(--navy);
    display: flex; align-items: center; justify-content: space-around;
    padding: 0 20px;
  }
  .contact-item { display: flex; align-items: center; gap: 8px; color: var(--band-text); font-size: 9px; line-height: 12px; }
  .contact-item svg { width: 20px; height: 20px; flex: none; }
</style>
</head>
<body>
  <main class="letterhead">
    <div class="brand">Ortoplena</div>

    <section class="recipient">
      <div class="recipient__label">TO</div>
      <div class="recipient__name">Paulo Andrade</div>
      <div class="recipient__line">Recursos Humanos</div>
      <div class="recipient__line">Estúdio Norte</div>
      <div class="recipient__line">Rua das Acácias, 120</div>
      <div class="recipient__line">São Paulo</div>
    </section>

    <section class="letter-body">
      <p>Acreditamos que a educação transforma pessoas e que pessoas transformam o mundo. Por isso, oferecemos cursos de ortodontia para dentistas já formados, com turmas reduzidas, professores experientes e acompanhamento clínico em cada etapa. Nosso objetivo é desenvolver profissionais seguros, atualizados e preparados para cuidar da saúde bucal de seus pacientes com ética, técnica e atenção verdadeira a cada sorriso atendido.</p>
      <p>Gostaríamos de apresentar a nova grade de pós-graduação e os cursos livres previstos para o próximo semestre, com vagas limitadas e condições especiais para inscrições antecipadas.</p>
      <p>Ficamos à disposição para esclarecer qualquer dúvida sobre os cursos.</p>
      <p>Além da ortodontia, mantemos cursos em outras áreas da odontologia, sempre com foco na prática clínica e na manutenção da saúde geral do paciente. Cada módulo combina aulas teóricas, atendimento supervisionado e discussão de casos reais, permitindo que o aluno aplique imediatamente o que aprendeu em seu consultório e acompanhe os resultados.</p>
      <p>Sabemos que um sorriso saudável eleva a autoestima e muda a forma como cada pessoa se relaciona com o mundo. É por isso que investimos em estrutura, materiais de qualidade e uma equipe dedicada a formar dentistas mais confiantes. Convidamos você a conhecer nossa sede, assistir a uma aula aberta e conversar com nossos coordenadores sobre o melhor caminho para a sua carreira profissional.</p>
      <p>Agradecemos a atenção e aguardamos seu contato para agendar uma visita à nossa escola.</p>
    </section>

    <div class="signature" role="img" aria-label="Assinatura manuscrita de Rafael Monteiro"></div>
    <div class="signer">
      <div class="signer__name">Rafael Monteiro</div>
      <div class="signer__role">Diretor Geral</div>
    </div>

    <footer class="contact-band">
      <div class="contact-item">
        <svg viewBox="0 0 20 20"><circle cx="10" cy="10" r="10" fill="#fff"/><path d="M7 5.5l1.6 0 .8 2.4-1.1.8a6 6 0 0 0 2.9 2.9l.8-1.1 2.4.8v1.6c0 .6-.5 1.1-1.1 1.1A7.8 7.8 0 0 1 5.9 6.6c0-.6.5-1.1 1.1-1.1z" fill="var(--navy)"/></svg>
        <span>11 4020 1357<br>11 4020 1358</span>
      </div>
      <div class="contact-item">
        <svg viewBox="0 0 20 20"><circle cx="10" cy="10" r="10" fill="#fff"/><rect x="5" y="6.5" width="10" height="7" rx="1" fill="var(--navy)"/><path d="M5.3 7l4.7 3.6L14.7 7" stroke="#fff" stroke-width="0.9" fill="none"/></svg>
        <span>contato@ortoplena.com.br</span>
      </div>
      <div class="contact-item">
        <svg viewBox="0 0 20 20"><circle cx="10" cy="10" r="10" fill="#fff"/><circle cx="10" cy="10" r="4.8" fill="none" stroke="var(--navy)" stroke-width="1.1"/><ellipse cx="10" cy="10" rx="2" ry="4.8" fill="none" stroke="var(--navy)" stroke-width="1"/><path d="M5.2 10h9.6" stroke="var(--navy)" stroke-width="1"/></svg>
        <span>www.ortoplena.com.br</span>
      </div>
      <div class="contact-item">
        <svg viewBox="0 0 20 20"><circle cx="10" cy="10" r="10" fill="#fff"/><path d="M10 4.5a3.8 3.8 0 0 0-3.8 3.8c0 2.9 3.8 7.2 3.8 7.2s3.8-4.3 3.8-7.2A3.8 3.8 0 0 0 10 4.5z" fill="var(--navy)"/><circle cx="10" cy="8.3" r="1.4" fill="#fff"/></svg>
        <span>Endereço Completo<br>Bairro - Cidade - Estado - Cep</span>
      </div>
    </footer>
  </main>
</body>
</html>
```